Business Card for my Photography/Video Business

I would like the card to say Event Photographer and Videographer. I like the Black and Gold look to it as well but open to other options. I don't want it to be super vibrant or colorful. Simple, elegant and professional

```html
<!DOCTYPE html>
<html lang="en">
<head>
<meta charset="utf-8">
<title>Halden Studio – Business Card</title>
<link href="https://fonts.googleapis.com/css2?family=Montserrat:wght@300&family=Open+Sans:wght@400&display=swap" rel="stylesheet">
<style>
  :root {
    --backdrop: #4a3e36;
    --card: #050506;
    --gold: #d4ae45;
    --gold-soft: #c9a649;
    --ink-light: #ecebe6;
    --rule: #8a7a52;
  }
  * { box-sizing: border-box; margin: 0; padding: 0; }
  html, body { width: 1200px; height: 1200px; overflow: hidden; }
  body {
    background: var(--backdrop);
    display: flex;
    flex-direction: column;
    align-items: center;
    justify-content: center;
    gap: 60px;
  }
  .card {
    position: relative;
    width: 860px;
    height: 491px;
    background: var(--card);
    box-shadow: 0 14px 30px rgba(0,0,0,0.35);
  }
  .brand__name {
    font-family: "Montserrat", sans-serif;
    font-weight: 300;
    font-size: 44px;
    letter-spacing: 1px;
    color: var(--gold);
    white-space: nowrap;
  }
  .card--front {
    display: flex;
    align-items: center;
    justify-content: center;
  }
  .card--back .brand {
    position: absolute;
    left: 70px;
    top: 245px;
    width: 400px;
    transform: translateY(-50%);
    text-align: center;
  }
  .card--back .brand__name { font-size: 36px; }
  .divider {
    position: absolute;
    left: 505px;
    top: 130px;
    width: 1px;
    height: 230px;
    background: var(--rule);
  }
  .contact {
    position: absolute;
    left: 532px;
    top: 120px;
    color: var(--ink-light);
    font-family: "Open Sans", sans-serif;
    font-size: 15px;
    line-height: 1.35;
  }
  .contact__name {
    font-family: "Montserrat", sans-serif;
    font-weight: 300;
    font-size: 34px;
    color: var(--gold-soft);
    line-height: 1.1;
  }
  .contact__role {
    font-size: 15px;
    margin-bottom: 22px;
  }
  .contact__row {
    display: flex;
    align-items: flex-start;
    gap: 12px;
  }
  .contact__row svg { width: 15px; height: 15px; flex: none; margin-top: 2px; fill: var(--ink-light); }
  .contact__row--address { margin-bottom: 18px; }
</style>
</head>
<body>
  <section class="card card--front">
    <div class="brand">
      <span class="brand__name">Halden Studio</span>
    </div>
  </section>

  <section class="card card--back">
    <div class="brand">
      <span class="brand__name">Halden Studio</span>
    </div>
    <span class="divider"></span>
    <div class="contact">
      <p class="contact__name">John Doe</p>
      <p class="contact__role">Photographer</p>
      <div class="contact__row contact__row--address">
        <svg viewBox="0 0 16 16" aria-hidden="true"><path d="M8 1a5 5 0 0 0-5 5c0 3.6 5 9 5 9s5-5.4 5-9a5 5 0 0 0-5-5zm0 7a2 2 0 1 1 0-4 2 2 0 0 1 0 4z"/></svg>
        <p>Dummy city<br>Dummy Country Land</p>
      </div>
      <div class="contact__row">
        <svg viewBox="0 0 16 16" aria-hidden="true"><path d="M2 5c0-2 2.5-3 6-3s6 1 6 3v1h-3V5H5v1H2zM4 7h8l2 6H2z"/></svg>
        <p>1-234-56789</p>
      </div>
      <div class="contact__row">
        <svg viewBox="0 0 16 16" aria-hidden="true"><path d="M8 1a7 7 0 1 0 0 14A7 7 0 0 0 8 1zm0 1.5c.8 1 1.4 2.5 1.6 4.5H6.4C6.6 5 7.2 3.5 8 2.5zM2.6 9h2.3c.1 1.6.5 3 1.1 4A5.6 5.6 0 0 1 2.6 9zm0-2A5.6 5.6 0 0 1 6 3c-.6 1-1 2.4-1.1 4zm5.4 6.5c-.8-1-1.4-2.5-1.6-4.5h3.2c-.2 2-.8 3.5-1.6 4.5zM10 13c.6-1 1-2.4 1.1-4h2.3A5.6 5.6 0 0 1 10 13zm1.1-6C11 5.4 10.6 4 10 3a5.6 5.6 0 0 1 3.4 4z"/></svg>
        <p>www.haldenstudio.com</p>
      </div>
      <div class="contact__row">
        <svg viewBox="0 0 16 16" aria-hidden="true"><path d="M1 3h14v10H1zm1.5 1.3v.4L8 8.8l5.5-4.1v-.4z"/></svg>
        <p>john@haldenstudio.com</p>
      </div>
    </div>
  </section>
</body>
</html>
```